Business Card for New Business

Please design a business card using our logo and font files. This is only one card for one person, as listed in details section.

Industry/Entity Type

Business

Contact Information for Business Card

Carl Voserby

Phone 541.318.6624
Cell 541.581.4096
Email carl@moltravex.com

www.moltravex.com

Address
18250 Brennick Lane #314
Halvern, OR 97412

Font styles to use
Sans Serif

Requirements
Must have
• Information listed in detail section. Must be standard card size.

```html
<!DOCTYPE html>
<html lang="en">
<head>
<meta charset="utf-8">
<title>Moltravex – Business Card</title>
<link rel="stylesheet" href="https://fonts.googleapis.com/css2?family=Questrial&family=Didact+Gothic&display=swap">
<style>
  :root {
    --page: #e4e4e4;
    --card-white: #ffffff;
    --brand-red: #c9372f;
    --brand-orange: #d2592a;
    --ink: #1d1d1d;
    --ink-soft: #4a4a4a;
    --muted: #8a8a8a;
    --blush: #fbe2e1;
    --divider: #e8a29d;
  }
  * { box-sizing: border-box; margin: 0; padding: 0; }
  html, body { width: 1200px; height: 1200px; overflow: hidden; }
  body {
    background: var(--page);
    font-family: "Questrial", "Didact Gothic", sans-serif;
    color: var(--ink);
    display: flex;
    flex-direction: column;
    align-items: center;
    justify-content: center;
    gap: 80px;
  }
  .card {
    position: relative;
    width: 700px;
    height: 400px;
    overflow: hidden;
    box-shadow: 0 10px 30px rgba(0,0,0,0.18);
  }

  /* Front */
  .card-front { background: var(--card-white); }
  .front-brand {
    position: absolute;
    left: 48px; top: 64px;
    display: flex; align-items: center; gap: 8px;
  }
  .brand-dot {
    width: 20px; height: 20px; border-radius: 50%;
    background: var(--brand-red);
  }
  .front-brand .brand-name {
    font-size: 44px; line-height: 1; color: var(--brand-red);
    letter-spacing: 0.5px;
  }
  .front-divider {
    position: absolute; left: 322px; top: 18px;
    width: 2px; height: 130px; background: var(--divider);
  }
  .person { position: absolute; left: 366px; top: 86px; }
  .person-name { font-size: 26px; letter-spacing: 0.6px; color: var(--ink); }
  .person-role {
    font-size: 17px; font-style: italic; color: var(--muted); margin-top: 6px;
    font-family: "Questrial", sans-serif;
  }
  .blush-circle {
    position: absolute; left: 100px; top: 184px;
    width: 134px; height: 134px; border-radius: 50%;
    background: var(--blush);
  }
  .contacts {
    position: absolute; left: 344px; top: 234px;
    list-style: none;
    font-family: "Questrial", sans-serif;
    font-size: 19px; color: var(--ink-soft);
  }
  .contacts li { display: flex; align-items: flex-start; gap: 10px; line-height: 26px; }
  .contacts svg { flex: none; margin-top: 5px; }
  .web-tab {
    position: absolute; left: 0; bottom: 0;
    width: 332px; height: 50px;
    background: var(--brand-red);
    border-top-right-radius: 40px;
    color: var(--card-white);
    font-size: 18px; letter-spacing: 0.4px;
    display: flex; align-items: center; padding-left: 50px;
  }

  /* Back */
  .card-back {
    background: linear-gradient(110deg, var(--brand-red) 0%, var(--brand-orange) 100%);
    display: flex; align-items: center; justify-content: center;
  }
  .back-brand { display: flex; align-items: center; gap: 14px; }
  .back-brand .brand-dot { width: 38px; height: 38px; background: var(--ink); }
  .back-brand .brand-name { font-size: 88px; line-height: 1; color: var(--ink); letter-spacing: 1px; }
</style>
</head>
<body>

  <section class="card card-front" aria-label="Business card front">
    <div class="front-brand">
      <span class="brand-dot"></span>
      <span class="brand-name">moltravex</span>
    </div>
    <div class="front-divider"></div>
    <div class="person">
      <p class="person-name">Carl Voserby</p>
      <p class="person-role">Position</p>
    </div>
    <div class="blush-circle"></div>
    <ul class="contacts">
      <li>
        <svg width="16" height="16" viewBox="0 0 16 16" aria-hidden="true"><circle cx="8" cy="8" r="8" fill="#2b2b2b"/><rect x="5.5" y="3.5" width="5" height="9" rx="1" fill="none" stroke="#fff" stroke-width="1.2"/></svg>
        <span>541.581.4096</span>
      </li>
      <li>
        <svg width="16" height="16" viewBox="0 0 16 16" aria-hidden="true"><circle cx="8" cy="8" r="8" fill="#2b2b2b"/><path d="M4 6.5 Q8 3.5 12 6.5 L11 8 L9.5 7.2 L9.5 6.2 Q8 5.7 6.5 6.2 L6.5 7.2 L5 8 Z" fill="#fff"/><rect x="5" y="8.5" width="6" height="3" rx="0.5" fill="#fff"/></svg>
        <span>541.318.6624</span>
      </li>
      <li>
        <svg width="16" height="16" viewBox="0 0 16 16" aria-hidden="true"><circle cx="8" cy="8" r="8" fill="#2b2b2b"/><rect x="4" y="5" width="8" height="6" fill="none" stroke="#fff" stroke-width="1.1"/><path d="M4 5 L8 8.5 L12 5" fill="none" stroke="#fff" stroke-width="1.1"/></svg>
        <span>carl@moltravex.com</span>
      </li>
      <li>
        <svg width="16" height="16" viewBox="0 0 16 16" aria-hidden="true"><circle cx="8" cy="8" r="8" fill="#2b2b2b"/><path d="M8 13 L5 8.3 A3.4 3.4 0 1 1 11 8.3 Z" fill="#fff"/><circle cx="8" cy="6.6" r="1.3" fill="#2b2b2b"/></svg>
        <span>18250 Brennick Lane #314<br>Halvern, OR 97412</span>
      </li>
    </ul>
    <div class="web-tab">www.moltravex.com</div>
  </section>

  <section class="card card-back" aria-label="Business card back">
    <div class="back-brand">
      <span class="brand-dot"></span>
      <span class="brand-name">moltravex</span>
    </div>
  </section>

</body>
</html>
```